International Digitally Led Media Agency Requires a New Website

Brief Outline

• We are a growing business that has been established for approximately 2 years.

• Our current website did the job when Corvend Media began but it has not developed and progressed alongside the business (currently it does not represent nor portray the business appropriately).

• Corvend Media is a digitally led media agency that has numerous arms; 1) production based work (e.g. Paid Advertising, etc.) 2) consultancy and 3) Offline media (such as outdoor, TV, Radio)

• The business is globally focused and the website must reflect this.

• The new website is to portray the business more professionally with thought leadership at the forefront.

• The tone and voice of the website is to be clear, concise and straight talking.

• The website isn't to be a driver of new business (e.g. conversion based for enquiries) but is to support external new business activities. However, the website is to support the thought leadership marketing (specifically around content marketing - webinars, whitepapers, social, etc).

• We must be able to edit/upload/add content to the website very easily.

The current website is www.corvend-media.example

Current clients include
Kestrow - www.j&t.example
Folmary Trudesse - www.ft.example
KX Glow - www.kxglow.example
Lungwise UK - www.lungwise.example.uk
The Vantry Academy - www.vantry-academy.example.uk
Hale Retirement - www.haleretirement.example
Quillet Credit - www.quilletcredit.example.uk
DLMorvat - www.dl-morvat.example.uk
Perravine Lodging Collective - www.plc-lodging.example
Brindlewick - www.brindlewick.example
Varnique - www.varniqueit.example

Reason: We gave some delayed feedback to some desginers looking to enter the project and want to give them a chance to submit their designs.

Target Market(s)

Key decision makers within brands. Marketing Executives/Managers/Directors, Procurement Executives/Managers/Directors, Company Owners, CEO's /MD's

Industry/Entity Type

Business

Coding

Coded - Design and coding required

Number of Pages Required

5+ page

Font styles to use
Sans Serif

Requirements
Must have
• We definitely want video capability and the ability to add pages ourselves.
• We would like the layout to look something like
• HOME
•   
• 7dash3 > CASE STUDIES
• WHAT WE DO > CASE STUDIES
•  
• CONTACT
•  
• CLIENT LOGIN
Nice to have
• Social feeds

```html
<!DOCTYPE html>
<html lang="en">
<head>
<meta charset="utf-8">
<title>Corvend Media — Digitally Led Media Agency</title>
<link href="https://fonts.googleapis.com/css2?family=Montserrat:wght@400;600;700;800&family=Open+Sans:wght@300;400;600&display=swap" rel="stylesheet">
<style>
:root{
  --maroon:#86193a;
  --maroon-dark:#6e1430;
  --ink:#2b2b2b;
  --text:#555;
  --muted:#8a8a8a;
  --line:#e3e3e3;
  --white:#fff;
  --sky:#3fa9e6;
  --red:#d8322c;
  --client:#b3b3b3;
}
*{box-sizing:border-box;margin:0;padding:0}
html,body{width:1200px;height:3696px;overflow:hidden;background:var(--white)}
body{position:relative;font-family:"Open Sans",Arial,sans-serif;color:var(--text)}
.btn-outline{position:absolute;display:flex;align-items:center;justify-content:center;gap:10px;border:2px solid var(--maroon);border-radius:30px;color:var(--maroon);font-family:"Montserrat",sans-serif;font-weight:600;font-size:12px;letter-spacing:.5px;text-transform:uppercase;background:var(--white)}
.arrow{width:28px;height:10px}

/* header */
.site-header{position:absolute;top:0;left:0;width:1200px;height:94px;background:var(--white)}
.brand{position:absolute;left:99px;top:14px;display:flex;align-items:center;gap:12px}
.brand-mark{width:46px;height:46px;border:2px solid var(--maroon);border-radius:50%}
.brand-name{font-family:"Montserrat",sans-serif;font-weight:600;font-size:15px;letter-spacing:2px;color:var(--ink);line-height:1.1}
.brand-name small{display:block;font-size:8px;letter-spacing:2px;color:var(--muted);font-weight:400}
.main-nav a{position:absolute;top:40px;font-family:"Montserrat",sans-serif;font-size:13px;color:var(--ink);text-decoration:none;text-transform:uppercase}
.client-login{left:963px;top:29px;width:137px;height:38px;font-size:12px}

/* hero */
.hero{position:absolute;top:94px;left:0;width:1200px;height:507px;background:linear-gradient(180deg,#5a5a5e 0%,#4a4340 40%,#3a302b 75%,#2e2622 100%)}
.hero-title{position:absolute;top:268px;width:1200px;text-align:center;font-family:"Montserrat",sans-serif;font-weight:700;font-size:56px;color:var(--white)}
.hero-sub{position:absolute;top:340px;width:1200px;text-align:center;font-family:"Montserrat",sans-serif;font-weight:600;font-size:30px;color:var(--white)}
.hero-cta{position:absolute;left:515px;top:402px;width:170px;height:40px;border-radius:22px;background:var(--maroon-dark);color:var(--white);font-family:"Montserrat",sans-serif;font-weight:600;font-size:12px;display:flex;align-items:center;justify-content:center;gap:8px;text-transform:uppercase}

.section-title{position:absolute;width:1200px;text-align:center;font-family:"Montserrat",sans-serif;font-weight:700;font-size:24px;color:var(--ink);letter-spacing:.5px}
.section-intro{position:absolute;left:210px;width:780px;text-align:center;font-size:13px;line-height:24px;color:var(--text)}

/* services */
.service-card{position:absolute;top:870px;width:313px;height:182px;border:1.5px solid var(--maroon);text-align:center}
.service-icon{position:absolute;left:124px;top:-34px;width:66px;height:66px;border-radius:50%;background:var(--maroon);display:flex;align-items:center;justify-content:center}
.service-card h3{margin-top:52px;font-family:"Montserrat",sans-serif;font-weight:700;font-size:15px;color:var(--ink)}
.service-card p{margin:18px auto 0;width:250px;font-size:11.5px;line-height:21px;color:var(--muted)}

/* what we do */
.what-photo{position:absolute;left:99px;top:1160px;width:423px;height:422px;background:linear-gradient(135deg,#9c9c9c,#4a4a4a 60%,#2b2b2b)}
.what-title{position:absolute;left:410px;top:1128px;font-family:"Montserrat",sans-serif;font-weight:800;font-size:124px;line-height:1;color:#333;letter-spacing:-2px}
.what-sub{position:absolute;left:615px;top:1250px;font-family:"Montserrat",sans-serif;font-weight:700;font-size:60px;color:#c8c8c8;line-height:1}
.what-copy{position:absolute;left:621px;top:1342px;width:460px;font-size:11.5px;line-height:21px;color:var(--muted)}
.what-copy p+p{margin-top:16px}

/* news */
.news-item{position:absolute;width:260px}
.news-date{font-size:20px;color:var(--maroon)}
.news-text{margin-top:18px;font-size:14px;line-height:22px;color:var(--ink)}
.news-link{margin-top:10px;display:flex;align-items:center;gap:6px;font-size:10.5px;color:var(--muted)}
.news-link i{width:11px;height:11px;border-radius:50%;background:var(--maroon);display:inline-block}
.news-rule{position:absolute;height:1px;width:135px;background:var(--line)}

/* video */
.video-band{position:absolute;top:2200px;left:0;width:1200px;height:478px;background:radial-gradient(circle at 58% 22%,#f4e2b8 0%,#c99a57 18%,#8b5f2b 45%,#4a3318 80%)}
.video-label{position:absolute;top:2420px;font-weight:300;font-size:44px;line-height:56px;color:var(--white);white-space:nowrap}
.video-label-left{right:676px;text-align:right}
.video-label-right{left:676px}
.play{position:absolute;left:542px;top:2389px;width:116px;height:116px;border-radius:50%;background:var(--white);display:flex;align-items:center;justify-content:center}

/* social feed */
.feed-badge{position:absolute;left:584px;top:2748px;width:32px;height:32px;border-radius:50%;background:var(--sky)}
.feed-title{position:absolute;top:2804px;width:1200px;text-align:center;font-size:20px;font-weight:400;color:var(--maroon)}
.feed-text{position:absolute;left:290px;top:2850px;width:620px;text-align:center;font-size:16px;line-height:26px;color:var(--muted)}
.feed-meta{position:absolute;top:2922px;width:1200px;text-align:center;font-size:13px;color:var(--text)}
.feed-meta b{font-weight:400;color:var(--sky)}
.dots{position:absolute;left:578px;top:2972px;display:flex;gap:5px}
.dots span{width:8px;height:8px;border-radius:50%;background:#ddd}
.dots span:first-child{background:#9ac53c}

/* clients */
.client-row{position:absolute;top:3210px;left:99px;width:1002px;display:flex;justify-content:space-between;align-items:center}
.client-name{font-family:"Montserrat",sans-serif;font-weight:700;font-size:24px;color:var(--client);display:flex;align-items:center;gap:10px;white-space:nowrap}
.client-name .dot{width:18px;height:18px;border-radius:50%;background:var(--client)}

/* footer */
.footer-top{position:absolute;top:3331px;left:0;width:1200px;height:1px;background:var(--line)}
.footer-col{position:absolute;top:3388px}
.footer-col h4{font-family:"Montserrat",sans-serif;font-weight:700;font-size:12px;color:var(--ink);text-transform:uppercase;letter-spacing:.3px}
.footer-col ul{list-style:none;margin-top:20px}
.footer-col li{font-size:11.5px;line-height:22px;color:var(--text)}
.newsletter p{margin-top:16px;font-size:11px;color:var(--text)}
.email-field{margin-top:20px;width:300px;height:38px;border:1px solid var(--line);border-radius:20px;padding-left:18px;font-size:11px;color:#aaa;display:flex;align-items:center}
.contact-line{display:flex;gap:8px;align-items:center}
.footer-bottom{position:absolute;top:3597px;left:0;width:1200px;height:1px;background:var(--line)}
.copyright{position:absolute;left:104px;top:3638px;font-size:11px;color:var(--text)}
.social{position:absolute;left:806px;top:3628px;display:flex;align-items:center;gap:8px;font-size:11px;color:var(--text)}
.social i{width:34px;height:34px;border-radius:50%;background:var(--sky);display:inline-block}
.social i.red{background:var(--red)}
</style>
</head>
<body>

<header class="site-header">
  <div class="brand">
    <span class="brand-mark"></span>
    <span class="brand-name">CORVEND<small>MEDIA AGENCY</small></span>
  </div>
  <nav class="main-nav">
    <a style="left:530px">Home</a>
    <a style="left:620px">Our Work</a>
    <a style="left:740px">Who We Are</a>
    <a style="left:870px">Contact</a>
  </nav>
  <a class="btn-outline client-login">
    <svg width="14" height="12" viewBox="0 0 14 12"><path d="M1 6h8M6 3l3 3-3 3M10 1h3v10h-3" fill="none" stroke="#86193a" stroke-width="1.5"/></svg>
    Client Login
  </a>
</header>

<section class="hero" role="img" aria-label="Aerial photograph of a city skyline and river at dusk"></section>
<h1 class="hero-title">Got the feeling</h1>
<p class="hero-sub">your digital marketing just isn't quite ‘there’?</p>
<a class="hero-cta">
  <svg width="12" height="12" viewBox="0 0 24 24"><path d="M6.6 10.8a15 15 0 006.6 6.6l2.2-2.2a1 1 0 011-.25 11.4 11.4 0 003.6.57 1 1 0 011 1V20a1 1 0 01-1 1A17 17 0 013 4a1 1 0 011-1h3.5a1 1 0 011 1c0 1.25.2 2.45.57 3.57a1 1 0 01-.25 1z" fill="#fff"/></svg>
  Contact Here!
</a>

<h2 class="section-title" style="top:666px">WE PROVIDE</h2>
<p class="section-intro" style="top:720px">There are too many large agency networks. Consolidation is everywhere, giving clients less choice and choking media creativity for the benefit of perceived economies of scale. There are too few agencies being transparent.</p>

<article class="service-card" style="left:99px">
  <span class="service-icon"><svg width="30" height="30" viewBox="0 0 30 30"><path d="M5 25V12l7 4V12l7 4V6h5v19z" fill="#fff"/></svg></span>
  <h3>PRODUCTION BASED WORK</h3>
  <p>We make your brand famous. To do this we optimise your website or any digital assets you have, so they can be found online...</p>
</article>
<article class="service-card" style="left:444px">
  <span class="service-icon"><svg width="30" height="30" viewBox="0 0 30 30"><rect x="5" y="6" width="20" height="14" rx="3" fill="none" stroke="#fff" stroke-width="2"/><path d="M11 20l-2 5 6-5" fill="#fff"/></svg></span>
  <h3>CONSULTANCY</h3>
  <p>We make your brand famous. To do this we optimise your website or any digital assets you have, so they can be found online...</p>
</article>
<article class="service-card" style="left:788px">
  <span class="service-icon"><svg width="30" height="30" viewBox="0 0 30 30"><rect x="4" y="12" width="16" height="12" rx="2" fill="#fff"/><path d="M20 16l6-3v10l-6-3z" fill="#fff"/><circle cx="8" cy="8" r="3" fill="#fff"/><circle cx="16" cy="8" r="3" fill="#fff"/></svg></span>
  <h3>OFFLINE MEDIA</h3>
  <p>We make your brand famous. To do this we optimise your website or any digital assets you have, so they can be found online...</p>
</article>

<div class="what-photo" role="img" aria-label="Black and white photograph of a film crew operating a camera on set"></div>
<div class="what-title">What</div>
<div class="what-sub">we do?</div>
<div class="what-copy">
  <p>We make your brand famous. To do this we optimise your website or any digital assets you have, so they can be found online, whether that is through search engines or social media.</p>
  <p>Then we make sure your paid media is as efficient as possible. Your customer lives in the real world as well as online, so we have no restrictions. We work with our clients across organic search, paid search, display and social media as well as television, press and out of home advertising.</p>
</div>
<a class="btn-outline" style="left:621px;top:1545px;width:127px;height:34px;font-size:10px">Read More
  <svg class="arrow" viewBox="0 0 28 10"><path d="M0 5h26M22 1l4 4-4 4" fill="none" stroke="#86193a" stroke-width="1.3"/></svg></a>

<h2 class="section-title" style="top:1678px">LATEST NEWS</h2>

<article class="news-item" style="left:99px;top:1764px"><div class="news-date">07 June 2016</div><p class="news-text">Dana Holloway report and it is all mobile, mobile, mobile!</p><div class="news-link">Learn More <i></i></div></article>
<article class="news-item" style="left:476px;top:1764px"><div class="news-date">25 May 2016</div><p class="news-text">Dana Holloway report and it is all mobile, mobile, mobile!</p><div class="news-link">Learn More <i></i></div></article>
<article class="news-item" style="left:852px;top:1764px"><div class="news-date">19 May2016</div><p class="news-text">Dana Holloway report and it is all mobile, mobile, mobile!</p><div class="news-link">Learn More <i></i></div></article>
<span class="news-rule" style="left:99px;top:1903px"></span>
<span class="news-rule" style="left:476px;top:1903px"></span>
<span class="news-rule" style="left:852px;top:1903px"></span>
<article class="news-item" style="left:99px;top:1937px"><div class="news-date">12 June 2016</div><p class="news-text">Dana Holloway report and it is all mobile, mobile, mobile!</p><div class="news-link">Learn More <i></i></div></article>
<article class="news-item" style="left:476px;top:1937px"><div class="news-date">16 April 2016</div><p class="news-text">Dana Holloway report and it is all mobile, mobile, mobile!</p><div class="news-link">Learn More <i></i></div></article>
<article class="news-item" style="left:852px;top:1937px"><div class="news-date">07 June 2016</div><p class="news-text">Dana Holloway report and it is all mobile, mobile, mobile!</p><div class="news-link">Learn More <i></i></div></article>
<a class="btn-outline" style="left:518px;top:2099px;width:164px;height:36px;font-size:10px">View More News
  <svg class="arrow" viewBox="0 0 28 10"><path d="M0 5h26M22 1l4 4-4 4" fill="none" stroke="#86193a" stroke-width="1.3"/></svg></a>

<section class="video-band" role="img" aria-label="Video still of a silhouetted figure standing in a field at sunset"></section>
<span class="video-label video-label-left">Corvend Media</span>
<a class="play"><svg width="40" height="44" viewBox="0 0 40 44"><path d="M6 2l32 20-32 20z" fill="#bdbdbd"/></svg></a>
<span class="video-label video-label-right">Who We Are</span>

<span class="feed-badge"></span>
<h3 class="feed-title">5 actions we took out of Brightlane Summit UK</h3>
<p class="feed-text">Geo-bias is as important as gender/race. The profile of people who work in cities is not reflective of the population</p>
<p class="feed-meta">Why attend <b>#BrightlaneUK</b>? 2015 attendees <b>@Corvend_Media</b> share their takeaways</p>
<div class="dots"><span></span><span></span><span></span><span></span></div>

<h2 class="section-title" style="top:3048px">OUR CLIENTS</h2>
<p class="section-intro" style="top:3100px">There are too many large agency networks. Consolidation is everywhere, giving clients less choice and choking media creativity for the benefit of perceived economies of scale. There are too few agencies being transparent.</p>
<div class="client-row">
  <span class="client-name">VELMORA <span class="dot"></span></span>
  <span class="client-name">Kestrow</span>
  <span class="client-name">Duvane</span>
  <span class="client-name">Stagegate Tickets</span>
  <span class="client-name">Orrin</span>
</div>

<div class="footer-top"></div>
<div class="footer-col newsletter" style="left:104px">
  <h4>Newsletter Signup</h4>
  <p>Get our recent updates through your email id.</p>
  <div class="email-field">Enter your email id</div>
  <a class="btn-outline" style="position:relative;margin-top:18px;width:128px;height:36px;font-size:10px">Subscribe
    <svg class="arrow" viewBox="0 0 28 10"><path d="M0 5h26M22 1l4 4-4 4" fill="none" stroke="#86193a" stroke-width="1.3"/></svg></a>
</div>
<div class="footer-col" style="left:489px">
  <h4>Welcome</h4>
  <ul><li>Home</li><li>Our Work</li><li>Who we are</li><li>Contact</li><li>Client Login</li></ul>
</div>
<div class="footer-col" style="left:702px">
  <h4>Information</h4>
  <ul><li>Terms &amp; Conditions</li><li>Privacy Policy</li><li>Disclaimer</li><li>Sitemap</li></ul>
</div>
<div class="footer-col" style="left:891px">
  <h4>Contact Info</h4>
  <ul>
    <li>14 Penrose Row, London<br>W1X 0AA</li>
    <li class="contact-line"><svg width="12" height="10" viewBox="0 0 12 10"><rect x=".5" y=".5" width="11" height="9" fill="none" stroke="#86193a"/><path d="M.5 .5l5.5 5 5.5-5" fill="none" stroke="#86193a"/></svg>contact@corvend-media.example</li>
    <li class="contact-line"><svg width="12" height="12" viewBox="0 0 24 24"><path d="M6.6 10.8a15 15 0 006.6 6.6l2.2-2.2a1 1 0 011-.25 11.4 11.4 0 003.6.57 1 1 0 011 1V20a1 1 0 01-1 1A17 17 0 013 4a1 1 0 011-1h3.5a1 1 0 011 1c0 1.25.2 2.45.57 3.57a1 1 0 01-.25 1z" fill="#86193a"/></svg>+44 20 7946 0321</li>
  </ul>
</div>
<div class="footer-bottom"></div>
<p class="copyright">Copyright © 2016, Corvend Media. All rights reserved.</p>
<div class="social">Connect with our social network : <i></i><i></i><i class="red"></i></div>

</body>
</html>
```